Banner for Vet Hospital 5m x 1.2m - Heat Stroke

Meadowlark Pet Hospital needs a Heat Stroke Banner for Summer.
The banner will be 5000mm long and 1200mm tall.

Our region has been hot this year and this summer is going to be extremely hot.
I want to warn people about heat stroke.
I want you to create a heat stroke banner that conveys the symptoms of heat stroke.

Pictures are better than words.
There should be IMAGES and WORDS that can be seen from the road 30m away and maybe some smaller words for people to read as they walk past.

Here are some of the signs of Heat Stroke:
- Panting which increases as heatstroke progresses
- Drooling, salivating
- Agitation, restlessness
- Very red or pale gums
- Bright red tongue
- Increased heart rate
- Breathing distress
- Vomiting Diarrhea (possibly with blood)
- Signs of mental confusion, delirium
- Dizziness, staggering
- Lethargy, weakness
- Muscle tremors
- Seizures
- Collapsing and lying down
- Little to no urine production
- Coma

I have attached characters that we often use in our advertising. They are optional.
I have done a mock up of the design I imagine. You could refine this design or make your own....or both.

Target Market(s)

Women aged 20 to 50.

Industry/Entity Type

Veterinary

Font styles to use
Sans Serif

Colors
fbed22
f78f20
ec1f27
ffffff

Requirements
Must have
• Heat Stroke Symtpms.
• Heat Stroke Warning.
• Summer theme.
Nice to have
• Bright colours.

```html
<!DOCTYPE html>
<html lang="en">
<head>
<meta charset="utf-8">
<title>Heat Stroke – Meadowlark Pet Hospital</title>
<link rel="stylesheet" href="https://fonts.googleapis.com/css2?family=Luckiest+Guy&family=Nunito:wght@700;800;900&display=swap">
<style>
  :root {
    --sun-yellow: #fbed22;
    --summer-orange: #f78f20;
    --alert-red: #ec1f27;
    --white: #ffffff;
    --ink-brown: #5a3a1e;
    --deep-brown: #3d2412;
    --floor-light: #c77a3a;
    --floor-dark: #8a4a1f;
    --symptom-green: #5fb229;
    --dog-fur: #8c7a6b;
    --dog-fur-light: #b3a496;
  }
  * { margin: 0; padding: 0; box-sizing: border-box; }
  html, body { width: 1200px; height: 310px; overflow: hidden; background: var(--white); }

  .banner {
    position: relative;
    width: 1200px;
    height: 310px;
    overflow: hidden;
    border: 10px solid var(--white);
    border-left-width: 14px;
    border-right-width: 14px;
    background: linear-gradient(90deg, #fff8b0 0%, var(--sun-yellow) 30%, var(--sun-yellow) 45%, var(--summer-orange) 72%, var(--alert-red) 100%);
    font-family: "Nunito", "Arial Rounded MT Bold", sans-serif;
  }
  .sun-rays {
    position: absolute; inset: 0;
    background: repeating-conic-gradient(from 60deg at 10px 20px, rgba(255,255,255,0.55) 0deg 4deg, rgba(255,255,255,0) 4deg 10deg);
    -webkit-mask-image: radial-gradient(circle at 10px 20px, #000 0, #000 280px, transparent 620px);
    mask-image: radial-gradient(circle at 10px 20px, #000 0, #000 280px, transparent 620px);
  }
  .sun {
    position: absolute; left: -46px; top: -34px;
    width: 112px; height: 112px; border-radius: 50%;
    background: var(--summer-orange);
  }
  .floor { position: absolute; left: 0; bottom: 0; width: 1172px; height: 80px; }

  .title {
    position: absolute; left: 398px; top: 14px;
    display: flex; align-items: center; gap: 8px;
  }
  .title-sun { width: 58px; height: 58px; }
  .title-text {
    font-family: "Luckiest Guy", "Arial Black", sans-serif;
    font-size: 54px; letter-spacing: 2px; line-height: 1;
    color: var(--alert-red);
    background: linear-gradient(180deg, var(--sun-yellow) 0%, var(--summer-orange) 45%, var(--alert-red) 80%);
    -webkit-background-clip: text; background-clip: text;
    -webkit-text-fill-color: transparent;
    -webkit-text-stroke: 2px var(--deep-brown);
    filter: drop-shadow(3px 3px 0 var(--deep-brown)) drop-shadow(0 0 2px var(--white)) drop-shadow(0 0 2px var(--white));
    margin-top: 10px;
  }

  .dog-art { position: absolute; background: linear-gradient(180deg, var(--dog-fur-light), var(--dog-fur)); opacity: 0.85; }
  .dog-sitting { left: 82px; top: 54px; width: 144px; height: 196px; border-radius: 60px 60px 24px 24px; }
  .dog-lying { left: 382px; top: 136px; width: 256px; height: 118px; border-radius: 70px 60px 24px 24px; }
  .dog-collapsed { left: 736px; top: 136px; width: 266px; height: 120px; border-radius: 40px 70px 40px 30px; }

  .stage-arrow { position: absolute; width: 100px; height: 42px; }
  .stage-arrow.first { left: 250px; top: 146px; }
  .stage-arrow.second { left: 638px; top: 138px; }

  .symptom { position: absolute; font-weight: 800; line-height: 1; white-space: nowrap; }
  .symptom.brown { color: var(--ink-brown); }
  .symptom.green { color: var(--symptom-green); }
  .symptom.red { color: var(--alert-red); }
  .symptom.gold { color: var(--sun-yellow); }
  .panting { left: 134px; top: 46px; font-size: 21px; transform: rotate(8deg); transform-origin: left; }
  .drooling { left: 26px; top: 116px; font-size: 12px; font-weight: 700; }
  .agitation { left: 14px; top: 170px; font-size: 18px; transform: rotate(-5deg); }
  .breathing { left: 356px; top: 118px; font-size: 18px; transform: rotate(-5deg); }
  .confusion { left: 510px; top: 96px; font-size: 18px; font-weight: 700; transform: rotate(16deg); transform-origin: left; }
  .diarrhea { left: 298px; top: 194px; font-size: 21px; transform: rotate(-12deg); }
  .vomiting { left: 606px; top: 200px; font-size: 17px; }
  .tremors { left: 774px; top: 98px; font-size: 24px; transform: rotate(-8deg); transform-origin: left; }
  .collapse { left: 898px; top: 136px; font-size: 18px; font-weight: 700; transform: rotate(8deg); }
  .coma { left: 1046px; top: 198px; font-size: 22px; }

  .booking-card {
    position: absolute; left: 1034px; top: 4px;
    width: 112px; height: 174px;
    background: var(--white);
    box-shadow: 3px 4px 6px rgba(0,0,0,0.35);
    display: flex; flex-direction: column; align-items: center;
    padding-top: 4px;
  }
  .book-online {
    width: 94px; height: 62px;
    background: var(--alert-red);
    color: var(--white);
    font-weight: 800; font-size: 17px; line-height: 1.1;
    text-align: center;
    display: flex; align-items: center; justify-content: center;
    border-radius: 3px;
  }
  .clinic-name {
    margin-top: 26px;
    width: 96px;
    text-align: center;
    font-weight: 800; font-size: 14px; line-height: 1.15;
    color: var(--ink-brown);
  }
</style>
</head>
<body>
<main class="banner">
  <div class="sun-rays"></div>
  <div class="sun"></div>

  <svg class="floor" viewBox="0 0 1172 80" preserveAspectRatio="none" aria-hidden="true">
    <defs>
      <linearGradient id="floorShade" x1="0" y1="0" x2="0" y2="1">
        <stop offset="0" stop-color="var(--floor-light)"/>
        <stop offset="1" stop-color="var(--floor-dark)"/>
      </linearGradient>
    </defs>
    <path d="M0 14 Q300 0 600 8 T1172 4 L1172 80 L0 80 Z" fill="url(#floorShade)"/>
    <path d="M90 30 L230 30 L210 80 L60 80 Z" fill="var(--deep-brown)" opacity="0.85"/>
    <path d="M400 36 L640 34 L660 80 L380 80 Z" fill="var(--deep-brown)" opacity="0.85"/>
    <path d="M760 32 L1010 30 L1050 80 L780 80 Z" fill="var(--deep-brown)" opacity="0.85"/>
  </svg>

  <div class="title">
    <svg class="title-sun" viewBox="0 0 60 60" aria-hidden="true">
      <g stroke="var(--alert-red)" stroke-width="4" stroke-linecap="round">
        <line x1="30" y1="3" x2="30" y2="11"/><line x1="30" y1="49" x2="30" y2="57"/>
        <line x1="3" y1="30" x2="11" y2="30"/><line x1="49" y1="30" x2="57" y2="30"/>
        <line x1="11" y1="11" x2="17" y2="17"/><line x1="43" y1="43" x2="49" y2="49"/>
        <line x1="11" y1="49" x2="17" y2="43"/><line x1="43" y1="17" x2="49" y2="11"/>
      </g>
      <circle cx="30" cy="30" r="13" fill="var(--summer-orange)" stroke="var(--alert-red)" stroke-width="2"/>
    </svg>
    <h1 class="title-text">HEAT STROKE</h1>
  </div>

  <div class="dog-art dog-sitting" role="img" aria-label="Illustration: a panting, drooling dog sitting in the sun"></div>
  <div class="dog-art dog-lying" role="img" aria-label="Illustration: an exhausted dog lying down, breathing heavily"></div>
  <div class="dog-art dog-collapsed" role="img" aria-label="Illustration: a dog collapsed on its back, unconscious"></div>

  <svg class="stage-arrow first" viewBox="0 0 100 42" aria-hidden="true">
    <defs>
      <linearGradient id="arrowFill" x1="0" y1="0" x2="1" y2="0">
        <stop offset="0" stop-color="var(--summer-orange)"/>
        <stop offset="1" stop-color="var(--alert-red)"/>
      </linearGradient>
    </defs>
    <path d="M2 12 H62 V2 L98 21 L62 40 V30 H2 Z" fill="url(#arrowFill)" stroke="var(--deep-brown)" stroke-width="2.5" stroke-linejoin="round"/>
  </svg>
  <svg class="stage-arrow second" viewBox="0 0 100 42" aria-hidden="true">
    <path d="M2 12 H62 V2 L98 21 L62 40 V30 H2 Z" fill="url(#arrowFill)" stroke="var(--deep-brown)" stroke-width="2.5" stroke-linejoin="round"/>
  </svg>

  <span class="symptom brown panting">Excessive Panting</span>
  <span class="symptom green drooling">Drooling</span>
  <span class="symptom green agitation">Agitation</span>
  <span class="symptom brown breathing">Breathing Distress</span>
  <span class="symptom red confusion">Confussion</span>
  <span class="symptom green diarrhea">Diarrhea</span>
  <span class="symptom green vomiting">Vomiting</span>
  <span class="symptom brown tremors">Muscles Tremors</span>
  <span class="symptom gold collapse">Collapse</span>
  <span class="symptom brown coma">Coma</span>

  <aside class="booking-card">
    <div class="book-online">BOOK<br>ONLINE</div>
    <div class="clinic-name">MEADOWLARK PET HOSPITAL</div>
  </aside>
</main>
</body>
</html>
```